Saffron Ledger Works Flyer

We need a one page promotional piece that explains what our company does, and the benefits it provides in a simple, elegant, easy to understand way. I would like to print it on glossy heavyweight paper to give a feel of high quality and legitimacy. I will include the logo, the tag line, and the main benefits that the company offers.

Tag line concept, may not need these exact words. "Give us 5 minutes a day, and we will help you build a Saffron Ledger Works."

Key points...(exact wording not required if you think of a better way to say it)

Software easy enough for my grandpa to use.
Lets you use snail mail, email, texting, and social media to quickly market to your customers at very low cost.
Web based which allows you to launch media campaigns from your desktop, or smartphone in moments.
Quick 3 - 5 minute training videos which give you hard hitting, quick action tips that will help you make your business better today.
Live coaching calls to help motivate you to improve your business.
No contracts, or start up fees. One low price of $299 per month.

Restaurant owners

Restaurant

```html
<!DOCTYPE html>
<html lang="en">
<head>
<meta charset="utf-8">
<title>Saffron Ledger Works Flyer</title>
<link rel="stylesheet" href="https://fonts.googleapis.com/css2?family=Arimo:wght@400;700&family=Oswald:wght@500&family=Roboto+Slab:wght@700;900&display=swap">
<style>
  :root {
    --backdrop: #454441;
    --sky: #a6c7e8;
    --sky-light: #d6e7f6;
    --leaf: #5fa347;
    --leaf-dark: #23803a;
    --leaf-deep: #1d6a30;
    --lime: #c6df48;
    --mint: #a8d58c;
    --slate: #58595b;
    --ink: #222222;
    --stone: #5c5c5c;
    --white: #ffffff;
  }
  * { margin: 0; padding: 0; box-sizing: border-box; }
  html, body { width: 923px; height: 1200px; overflow: hidden; }
  body { background: var(--backdrop); position: relative; font-family: "Arimo", Arial, sans-serif; }

  .flyer {
    position: absolute; left: 69px; top: 92px; width: 785px; height: 1016px;
    background: radial-gradient(circle at 50% 27%, var(--sky-light) 0%, var(--sky) 55%);
    overflow: hidden;
  }

  .price-flag { position: absolute; left: 631px; top: 3px; width: 104px; height: 173px; }
  .price-flag svg { position: absolute; inset: 0; }
  .price-flag .price-text { position: absolute; inset: 0; text-align: center; color: var(--white); font-family: "Oswald", "Arial Narrow", sans-serif; }
  .price-just { display: block; margin-top: 22px; font-size: 27px; line-height: 1; color: var(--mint); }
  .price-amount { display: block; font-size: 46px; line-height: 1; margin-top: 2px; }
  .price-amount small { font-size: 26px; vertical-align: 14px; }
  .price-term { display: block; font-family: "Arimo", Arial, sans-serif; font-weight: 700; font-size: 15px; margin-top: 2px; color: var(--mint); }

  .brand-mark { position: absolute; left: 297px; top: 95px; width: 190px; height: 190px; border-radius: 50%; background: #eef3f8; }
  .brand-name {
    position: absolute; left: 0; width: 100%; top: 335px; text-align: center;
    font-family: "Roboto Slab", Rockwell, serif; font-weight: 900; color: var(--stone);
    font-size: 40px; line-height: 42px; letter-spacing: 1px;
  }

  .headline-ribbon { position: absolute; left: 0; top: 0; width: 785px; height: 700px; }
  .headline { position: absolute; left: 116px; top: 494px; width: 575px; text-align: center; color: var(--white); }
  .headline-main { display: block; font-family: "Roboto Slab", Rockwell, serif; font-weight: 900; font-size: 66px; line-height: 74px; }
  .headline-sub { display: block; font-family: "Arimo", Arial, sans-serif; font-weight: 400; font-size: 25px; line-height: 30px; letter-spacing: .3px; }

  .benefits { position: absolute; list-style: none; width: 310px; }
  .benefits.left { left: 66px; top: 686px; }
  .benefits.right { left: 426px; top: 686px; }
  .benefit { position: relative; padding-left: 52px; font-weight: 700; font-size: 14.5px; line-height: 17.5px; color: var(--ink); }
  .benefit::before {
    content: ""; position: absolute; left: 0; top: -4px; width: 40px; height: 40px;
    border-radius: 50%; background: var(--leaf); border: 3px solid var(--white);
  }
  .benefits .benefit + .benefit { margin-top: 15px; }

  .join-banner { position: absolute; left: 0; top: 900px; width: 785px; height: 56px; }
  .join-text {
    position: absolute; left: 0; top: 914px; width: 785px; text-align: center;
    font-family: "Oswald", "Arial Narrow", sans-serif; font-size: 20px; line-height: 26px; color: var(--lime);
  }
  .phone {
    position: absolute; left: 0; top: 955px; width: 785px; text-align: center;
    font-weight: 700; font-size: 28px; line-height: 36px; color: var(--stone);
  }
  .phone svg { width: 26px; height: 26px; vertical-align: -4px; margin-right: 4px; }
</style>
</head>
<body>
  <main class="flyer">
    <div class="price-flag">
      <svg viewBox="0 0 104 173" aria-hidden="true"><polygon points="0,0 104,0 104,173 52,150 0,173" fill="var(--leaf-dark)"/></svg>
      <div class="price-text">
        <span class="price-just">Just</span>
        <span class="price-amount"><small>$</small>000</span>
        <span class="price-term">per month</span>
      </div>
    </div>

    <div class="brand-mark" aria-hidden="true"></div>
    <h1 class="brand-name">SAFFRON<br>LEDGER<br>WORKS</h1>

    <svg class="headline-ribbon" viewBox="0 0 785 700" aria-hidden="true">
      <polygon points="59,540 176,540 176,653 59,653 95,597" fill="var(--leaf-dark)"/>
      <polygon points="749,540 632,540 632,653 749,653 713,597" fill="var(--leaf-dark)"/>
      <polygon points="116,620 176,620 176,653" fill="var(--leaf-deep)"/>
      <polygon points="691,620 632,620 632,653" fill="var(--leaf-deep)"/>
      <rect x="116" y="486" width="575" height="134" fill="var(--leaf)"/>
    </svg>
    <h2 class="headline">
      <span class="headline-main">BUILD YOUR</span>
      <span class="headline-sub">SAFFRON LEDGER WORKS</span>
    </h2>

    <ul class="benefits left">
      <li class="benefit">Software easy enough for my<br>grandpa to use.</li>
      <li class="benefit">Lets you use snail mail, email,<br>texting, and social media to<br>quickly market to your customers<br>at very low cost.</li>
      <li class="benefit">Web based which allows you to<br>launch media campaigns from<br>your desktop, or smartphone in<br>moments.</li>
    </ul>
    <ul class="benefits right">
      <li class="benefit">Quick 3 - 5 minute training videos<br>which give you hard hitting, quick<br>action tips that will help you make<br>your business better today.</li>
      <li class="benefit">Live coaching calls to help<br>motivate you to improve your<br>business.</li>
      <li class="benefit">No contracts, or start up fees.<br>One low price of $ 000 per month.</li>
    </ul>

    <svg class="join-banner" viewBox="0 0 785 56" aria-hidden="true">
      <polygon points="71,6 717,6 700,27 717,48 71,48 88,27" fill="var(--slate)"/>
    </svg>
    <p class="join-text">JOIN NOW: WWW.SAFFRONLEDGERWORKS.COM</p>
    <p class="phone">
      <svg viewBox="0 0 26 26" aria-hidden="true">
        <circle cx="13" cy="13" r="11.5" fill="none" stroke="var(--stone)" stroke-width="2"/>
        <path d="M9 7 h3 l1 3 -2 1.5 q1 3 3.5 4.5 l1.5 -2 3 1 v3 q-1 1.5 -3 1 q-7 -2 -8 -9 q0 -2 1 -3z" fill="var(--stone)"/>
      </svg>555-014-2290
    </p>
  </main>
</body>
</html>
```